Letterhead Design Project

We are looking for a simple letterhead design that reflects our core purpose. We help our clients gain clarity and focus but we are there to help them execute. The letterhead design would mainly be utilised for engagement letters and contracts.

Target Market(s)

The customers of our business are large corporate organisations.

Requirements
Must have
• The letterhead must have the company logo
The font used must tie in to the font used in the company logo

Must have the following business details
Address: Level 10, 27 Harlow Lane, Melbourne, Australia, 3000
Phone: +61 3 527 948 183
Fax: +61 3 9042 5317
Website: www.bovrin-u.com.au
Twiiter: @bovrin_u

```html
<!DOCTYPE html>
<html lang="en">
<head>
<meta charset="utf-8">
<title>Bovrin-u Letterhead</title>
<link rel="stylesheet" href="https://fonts.googleapis.com/css2?family=Open+Sans:wght@400;600&display=swap">
<style>
  :root {
    --brand-blue: #1d4fe6;
    --ink: #1a1a1a;
    --paper: #ffffff;
    --backdrop: #e9e9e9;
    --rule: #555555;
    --social: #4fc3f0;
  }
  * { margin: 0; padding: 0; box-sizing: border-box; }
  html, body { width: 927px; height: 1200px; overflow: hidden; }
  body {
    background: var(--backdrop);
    font-family: "Open Sans", Arial, sans-serif;
    position: relative;
  }
  .letterhead {
    position: absolute;
    left: 45px; top: 70px;
    width: 846px; height: 1096px;
    background: var(--paper);
    box-shadow: 0 2px 8px rgba(0,0,0,0.25);
    overflow: hidden;
  }
  .brand {
    position: absolute;
    left: 28px; top: 32px;
  }
  .brand-name {
    font-weight: 400;
    font-size: 60px;
    line-height: 1;
    color: var(--brand-blue);
    letter-spacing: 0.5px;
  }
  .brand-suffix {
    display: block;
    text-align: right;
    font-size: 8px;
    color: var(--brand-blue);
    margin-top: -2px;
    padding-right: 70px;
  }
  .contact {
    position: absolute;
    left: 665px; top: 30px;
    border-left: 1px solid var(--rule);
    padding: 4px 0 6px 10px;
    list-style: none;
  }
  .contact li {
    display: flex;
    align-items: center;
    gap: 6px;
    font-size: 12.5px;
    line-height: 18px;
    color: var(--ink);
  }
  .contact svg { width: 12px; height: 12px; flex: none; }
  .footer-band {
    position: absolute;
    left: 0; bottom: 0;
    width: 100%; height: 44px;
    background: var(--brand-blue);
  }
  .footer-address {
    position: absolute;
    left: 110px; top: 10px;
    color: var(--paper);
    font-size: 16px;
    letter-spacing: 0.6px;
  }
  .footer-mark {
    position: absolute;
    left: 28px; bottom: 12px;
    width: 66px; height: 66px;
  }
</style>
</head>
<body>
  <main class="letterhead">
    <header class="brand">
      <div class="brand-name">Bovrin-u</div>
      <span class="brand-suffix">Pty Ltd</span>
    </header>

    <ul class="contact">
      <li>
        <svg viewBox="0 0 12 12" aria-hidden="true"><circle cx="6" cy="6" r="5" fill="none" stroke="#1a1a1a" stroke-width="1"/><path d="M4 3.5 L5 3 L5.6 4.6 L5 5.1 Q5.6 6.6 6.9 7 L7.4 6.4 L9 7 L8.5 8 Q5 8.4 4 3.5Z" fill="#1a1a1a"/></svg>
        +61 3 527 948 183
      </li>
      <li>
        <svg viewBox="0 0 12 12" aria-hidden="true"><path d="M1 5 Q6 1 11 5 L10 6 L8 5 L8 4 Q6 3.3 4 4 L4 5 L2 6Z" fill="#1a1a1a"/><rect x="3" y="6.5" width="6" height="4" rx="1" fill="#1a1a1a"/></svg>
        +61 3 9042 5317
      </li>
      <li>
        <svg viewBox="0 0 12 12" aria-hidden="true"><circle cx="6" cy="6" r="5" fill="none" stroke="#1a1a1a"/><ellipse cx="6" cy="6" rx="2.2" ry="5" fill="none" stroke="#1a1a1a" stroke-width="0.8"/><line x1="1" y1="6" x2="11" y2="6" stroke="#1a1a1a" stroke-width="0.8"/></svg>
        www.bovrin-u.com.au
      </li>
      <li>
        <svg viewBox="0 0 12 12" aria-hidden="true"><rect x="0.5" y="0.5" width="11" height="11" rx="2" fill="var(--social)"/></svg>
        @bovrin_u
      </li>
    </ul>

    <footer class="footer-band">
      <p class="footer-address">Level 10, 27 Harlow Lane, Melbourne, Australia, 3000</p>
    </footer>
    <svg class="footer-mark" viewBox="0 0 66 66" aria-hidden="true">
      <circle cx="33" cy="33" r="31" fill="var(--paper)" stroke="var(--brand-blue)" stroke-width="3"/>
    </svg>
  </main>
</body>
</html>
```